PowerPoint Design TELM

I have now selected the logo for my consultancy company. I need some innovative design for my Powerpoint slides. The audience is senior executives in international banks predominantly in Asia, but also in the Middle East, Africa and Latin America.
My company advises them on solutions to be able to grow their business.
This is my main means of hooking the clients and it is crucial to the success of my business.
I will update the file to a vector file in a few hours.

I am looking for a complete template.

Senior hard nosed executives in international Banks

```html
<!DOCTYPE html>
<html lang="en">
<head>
<meta charset="utf-8">
<title>TELM Slide Template</title>
<link rel="stylesheet" href="https://fonts.googleapis.com/css2?family=Exo+2:wght@300;400;500&family=Arimo:wght@400&display=swap">
<style>
  :root {
    --green-deep: #05964f;
    --green-mid: #1cc38a;
    --green-glow: #3cecd6;
    --title-accent: #109a55;
    --ink: #3b3b3b;
    --body-text: #4a4a4a;
    --body-bold: #333333;
    --canvas-top: #f7f7f7;
    --canvas-bottom: #e6e8ee;
    --card-bg: #ffffff;
    --card-line: #dadada;
    --footer-bg: #f8f8f8;
    --footer-line: #cfd3d8;
  }
  * { margin: 0; padding: 0; box-sizing: border-box; }
  html, body { width: 1200px; height: 900px; overflow: hidden; }
  body { font-family: "Exo 2", sans-serif; background: #ffffff; }

  .slide {
    position: relative;
    width: 1200px;
    height: 900px;
    overflow: hidden;
    background: linear-gradient(180deg, var(--canvas-top) 0%, #f1f2f4 60%, var(--canvas-bottom) 100%);
  }

  .slide-header {
    position: absolute;
    left: 0; top: 0;
    width: 1200px; height: 96px;
    background:
      radial-gradient(ellipse 360px 140px at 560px 40px, var(--green-glow) 0%, rgba(60,236,214,0) 100%),
      linear-gradient(90deg, var(--green-deep) 0%, var(--green-mid) 40%, var(--green-mid) 60%, var(--green-deep) 100%);
    border-bottom: 2px solid #e9ecee;
  }
  .slide-title {
    position: absolute;
    left: 30px; top: 20px;
    font-weight: 400;
    font-size: 43px;
    color: #ffffff;
    letter-spacing: 0.5px;
  }

  .backdrop-texture {
    position: absolute;
    left: 0; top: 98px;
    width: 820px; height: 714px;
    background: radial-gradient(ellipse 520px 420px at 300px 300px, rgba(200,203,208,0.35) 0%, rgba(200,203,208,0) 100%);
  }

  .content {
    position: absolute;
    left: 66px; top: 155px;
    width: 532px;
  }
  .content-title {
    font-weight: 400;
    font-size: 34px;
    color: var(--ink);
    margin-bottom: 22px;
  }
  .content-title .accent { color: var(--title-accent); }
  .content p {
    font-weight: 400;
    font-size: 20px;
    line-height: 39px;
    color: var(--body-text);
    margin-bottom: 39px;
  }
  .content .line {
    display: block;
    white-space: nowrap;
    text-align: justify;
    text-align-last: justify;
  }
  .content .line.last { text-align-last: left; }
  .content p strong { font-weight: 500; color: var(--body-bold); }

  .photo-slot {
    position: absolute;
    left: 708px;
    width: 446px;
    height: 197px;
    background: var(--card-bg);
    border: 1px solid var(--card-line);
    border-radius: 6px;
    box-shadow: 0 2px 6px rgba(0,0,0,0.12);
    display: flex;
    align-items: center;
    justify-content: center;
    font-weight: 500;
    font-size: 21px;
    color: #555555;
  }
  .photo-slot.first { top: 226px; }
  .photo-slot.second { top: 496px; }

  .slide-footer {
    position: absolute;
    left: 0; top: 812px;
    width: 1200px; height: 88px;
    background: linear-gradient(180deg, #ffffff 0%, var(--footer-bg) 100%);
    border-top: 2px solid var(--footer-line);
  }
  .copyright {
    position: absolute;
    left: 28px; top: 36px;
    font-family: "Arimo", sans-serif;
    font-size: 19px;
    color: #1f1f1f;
  }
  .brand-name {
    position: absolute;
    right: 30px; top: 20px;
    font-weight: 400;
    font-size: 40px;
    color: var(--ink);
  }
</style>
</head>
<body>
  <main class="slide">
    <header class="slide-header">
      <h1 class="slide-title">Insert Title Here</h1>
    </header>

    <div class="backdrop-texture" role="img" aria-label="Soft grey halftone dot texture"></div>

    <section class="content">
      <h2 class="content-title">Content <span class="accent">Title Here</span></h2>
      <p>
        <span class="line"><strong>Lorem ipsum dolor sit ipsum</strong> Lorem ipsum dolor sit</span>
        <span class="line">ipsum Lorem ipsum Lorem ipsum dolor sit ipsum Lorem</span>
        <span class="line last">ipsum dolor sit ipsum Lorem ipsum.</span>
      </p>
      <p>
        <span class="line"><strong>Lorem ipsum dolor sit</strong> ipsum Lorem ipsum dolor sit</span>
        <span class="line">ipsum Lorem ipsum Lorem ipsum dolor sit ipsum Lorem</span>
        <span class="line last">ipsum dolor sit ipsum Lorem ipsum.</span>
      </p>
      <p>
        <span class="line">Lorem ipsum dolor sit ipsum Lorem ipsum dolor sit</span>
        <span class="line">ipsum Lorem ipsum Lorem ipsum dolor sit ipsum Lorem</span>
        <span class="line last">ipsum dolor sit ipsum Lorem ipsum.</span>
      </p>
    </section>

    <div class="photo-slot first" role="img" aria-label="Photo placeholder">Photo Here</div>
    <div class="photo-slot second" role="img" aria-label="Photo placeholder">Photo Here</div>

    <footer class="slide-footer">
      <span class="copyright">Copyright Text here</span>
      <span class="brand-name">TELM</span>
    </footer>
  </main>
</body>
</html>
```